Commercial Piping Company Needs A Modern Business Card

We need a clean business card for our commercial pipe lining company. We would like to see a mock up in two color schemes: Black, Grey and Blue and Black, Grey and Orange. We are in the piping industry, but want a professional, clean and modern look to the card.

Industry/Entity Type

Plumbing

Contact Information for Business Card

Name: Mark Telford
Title: Managing Partner
Phone: 608.352.9174
Email: Mark@VeltaSpan.Net

Requirements
Must have
• Back Side Should Have a White Back Ground with Full Logo. Front I would like to see a couple lay outs for contact info. Also the final card will have rounded edges, so please take that into account for printing.
Nice to have
• Two Color Palette Examples
Should not have
• No need for an address line

```html
<!DOCTYPE html>
<html lang="en">
<head>
<meta charset="utf-8">
<title>VeltaSpan Business Card</title>
<link rel="stylesheet" href="https://fonts.googleapis.com/css2?family=Montserrat:wght@400;500;700&family=Questrial&display=swap">
<style>
  :root {
    --page: #f3f3f3;
    --card-top: #ffffff;
    --card-bottom: #e6e6e6;
    --charcoal: #3f3f3f;
    --ink: #2f3a40;
    --orange: #f7941d;
    --orange-deep: #f26f21;
    --orange-light: #fbb03b;
  }
  * { margin: 0; padding: 0; box-sizing: border-box; }
  html, body { width: 1176px; height: 1200px; overflow: hidden; }
  body { background: var(--page); position: relative; font-family: "Montserrat", sans-serif; }

  .card {
    position: absolute;
    left: 218px;
    width: 740px;
    height: 418px;
    border-radius: 20px;
    overflow: hidden;
    background: linear-gradient(180deg, var(--card-top) 35%, var(--card-bottom) 100%);
  }
  .card--logo { top: 151px; }
  .card--contact { top: 654px; }
  .card__swoosh { position: absolute; inset: 0; width: 100%; height: 100%; }

  .brand { position: absolute; display: flex; align-items: center; }
  .brand__dot { border-radius: 50%; background: var(--charcoal); flex: none; }
  .brand__name {
    font-family: "Questrial", sans-serif;
    color: var(--charcoal);
    letter-spacing: 0.02em;
    line-height: 1;
  }
  .brand__tag {
    font-family: "Questrial", sans-serif;
    color: var(--charcoal);
    line-height: 1.05;
    letter-spacing: 0.06em;
  }

  .brand--large { left: 115px; top: 128px; gap: 22px; }
  .brand--large .brand__dot { width: 106px; height: 106px; }
  .brand--large .brand__name { font-size: 60px; }
  .brand--large .brand__tag { font-size: 22px; margin-top: 4px; }

  .brand--small { left: 558px; top: 300px; flex-direction: column; align-items: center; gap: 4px; }
  .brand--small .brand__dot { width: 32px; height: 32px; }
  .brand--small .brand__name { font-size: 21px; }
  .brand--small .brand__tag { font-size: 7.6px; text-align: center; letter-spacing: 0.03em; }

  .person { position: absolute; left: 44px; top: 60px; color: var(--ink); }
  .person__name { font-size: 26px; font-weight: 400; letter-spacing: 0.01em; }
  .person__name strong { font-weight: 700; }
  .person__title { font-size: 21px; font-weight: 500; margin-top: 4px; }
  .person__rule { width: 109px; height: 3px; background: var(--orange); margin-top: 10px; }

  .contacts { position: absolute; left: 41px; top: 179px; list-style: none; }
  .contacts__item { display: flex; align-items: center; height: 42px; margin-bottom: 20px; }
  .contacts__icon {
    width: 42px; height: 42px; border-radius: 50%;
    background: var(--orange); flex: none;
    display: flex; align-items: center; justify-content: center;
  }
  .contacts__icon svg { width: 22px; height: 22px; }
  .contacts__text { margin-left: 17px; font-size: 16px; font-weight: 500; color: var(--ink); }
</style>
</head>
<body>

<section class="card card--logo">
  <svg class="card__swoosh" viewBox="0 0 504 284" preserveAspectRatio="none" aria-hidden="true">
    <defs>
      <linearGradient id="orangeFlowA" x1="0" y1="1" x2="1" y2="0">
        <stop offset="0" stop-color="#fbb03b"/>
        <stop offset="1" stop-color="#f26f21"/>
      </linearGradient>
    </defs>
    <path d="M0,0 H100 Q40,20 0,62 Z" fill="#f7941d"/>
    <path d="M100,0 H150 Q60,40 0,112 V62 Q40,20 100,0 Z" fill="#3f3f3f"/>
    <path d="M504,8 C482,160 420,250 330,284 H504 Z" fill="#3f3f3f"/>
    <path d="M504,132 C452,232 350,274 190,284 H504 Z" fill="url(#orangeFlowA)"/>
  </svg>
  <div class="brand brand--large">
    <span class="brand__dot"></span>
    <div>
      <div class="brand__name">VELTASPAN</div>
      <div class="brand__tag">PIPE RESTORATION SOLUTIONS<br>INVESTIGATE • PLAN • DELIVER</div>
    </div>
  </div>
</section>

<section class="card card--contact">
  <svg class="card__swoosh" viewBox="0 0 504 284" preserveAspectRatio="none" aria-hidden="true">
    <defs>
      <linearGradient id="orangeFlowB" x1="0" y1="1" x2="1" y2="0">
        <stop offset="0" stop-color="#f26f21"/>
        <stop offset="1" stop-color="#fbb03b"/>
      </linearGradient>
    </defs>
    <path d="M504,5 C460,170 300,262 100,284 H504 Z" fill="#3f3f3f"/>
    <path d="M504,85 C432,200 322,266 150,284 H504 Z" fill="url(#orangeFlowB)"/>
  </svg>

  <div class="person">
    <div class="person__name"><strong>MARK</strong> TELFORD</div>
    <div class="person__title">Managing Partner</div>
    <div class="person__rule"></div>
  </div>

  <ul class="contacts">
    <li class="contacts__item">
      <span class="contacts__icon">
        <svg viewBox="0 0 24 24" fill="none" stroke="#fff" stroke-width="2" stroke-linejoin="round"><rect x="3" y="6" width="18" height="13" rx="1.5"/><path d="M3.5 7 L12 13.5 L20.5 7"/></svg>
      </span>
      <span class="contacts__text">Mark@VeltaSpan.Net</span>
    </li>
    <li class="contacts__item">
      <span class="contacts__icon">
        <svg viewBox="0 0 24 24" fill="none" stroke="#fff" stroke-width="2" stroke-linejoin="round"><path d="M6.5 3.5 L9.5 3.5 L11 8 L8.8 9.6 C9.9 11.9 12.1 14.1 14.4 15.2 L16 13 L20.5 14.5 L20.5 17.5 C20.5 19 19.3 20.5 17.5 20.5 C10 20 4 14 3.5 6.5 C3.5 4.8 4.9 3.5 6.5 3.5 Z"/></svg>
      </span>
      <span class="contacts__text">608.352.9174</span>
    </li>
    <li class="contacts__item">
      <span class="contacts__icon">
        <svg viewBox="0 0 24 24" fill="none" stroke="#fff" stroke-width="1.8"><circle cx="12" cy="12" r="8.5"/><ellipse cx="12" cy="12" rx="3.6" ry="8.5"/><path d="M3.5 12 H20.5 M5 7.5 H19 M5 16.5 H19"/></svg>
      </span>
      <span class="contacts__text">www.VeltaSpan.Net</span>
    </li>
  </ul>

  <div class="brand brand--small">
    <span class="brand__dot"></span>
    <div class="brand__name">VELTASPAN</div>
    <div class="brand__tag">PIPE RESTORATION SOLUTIONS<br>INVESTIGATE • PLAN • DELIVER</div>
  </div>
</section>

</body>
</html>
```